Succession & Estate Planning firm needs a double-sided one page client handout

We need a client hand-out that highlights the top 10 Reasons to get a Pension Plan. It will need the 10 reasons as headings, with a short description of each reason (attached Word doc). It should communicate that a Pension Plan is flexible and provides security. Our usual client is a business owner/medical professional/entrepreneur. Have a look at our website for more info about our business www.quorvane.ca Our logo colours are 83c242, 3b3839, d5d5d5 We like clean, modern, info-graphics, not too cluttered, not too loudWe would like the ability to update the text/content ourselves, in the future.

```html
<!DOCTYPE html>
<html lang="en">
<head>
<meta charset="utf-8">
<title>Top 10 Reasons – Quorvane Handout</title>
<link rel="stylesheet" href="https://fonts.googleapis.com/css2?family=Bebas+Neue&family=Didact+Gothic&display=swap">
<style>
  :root{
    --green:#83c242;
    --charcoal:#3b3839;
    --silver:#d5d5d5;
    --backdrop:#a9aaad;
    --paper:#ffffff;
    --tint:#e3f0d3;
    --text:#2f2d2e;
    --photo-dark:#34401f;
    --photo-mid:#56652f;
    --photo-warm:#6e5c3f;
  }
  *{margin:0;padding:0;box-sizing:border-box}
  html,body{width:1200px;height:859px;overflow:hidden}
  body{background:var(--backdrop);font-family:"Didact Gothic",sans-serif;color:var(--text);position:relative}

  .sheet{position:absolute;top:110px;width:497px;height:642px;background:var(--paper);overflow:hidden;box-shadow:0 6px 14px rgba(0,0,0,.18)}
  .sheet--front{left:86px;background:linear-gradient(180deg,#fff 0%,#fff 62%,var(--tint) 100%)}
  .sheet--back{left:630px;background:linear-gradient(180deg,var(--tint) 0%,#f3f8ec 22%,#fff 48%,#fff 100%)}

  .brand{position:absolute;font-family:"Didact Gothic",sans-serif;color:var(--charcoal);letter-spacing:.14em;display:flex;align-items:center;gap:6px}
  .brand-dot{width:9px;height:9px;border-radius:50%;background:var(--green)}
  .sheet--front .brand{right:38px;top:46px;font-size:22px}
  .sheet--back .brand{right:30px;top:30px;font-size:17px}

  .title{font-family:"Bebas Neue",sans-serif;color:var(--green);font-weight:400;line-height:1}
  .subtitle{font-weight:400;color:var(--text);line-height:1.05}
  .sheet--front .title{position:absolute;left:32px;top:24px;font-size:35px}
  .sheet--front .subtitle{position:absolute;left:33px;top:56px;font-size:19.5px;width:230px}
  .sheet--back .title{position:absolute;left:30px;top:19px;font-size:23px}
  .sheet--back .subtitle{position:absolute;left:31px;top:39px;font-size:12.5px}

  .hero{position:absolute;left:0;top:116px;width:100%;height:124px;
    background:linear-gradient(90deg,var(--photo-dark) 0%,var(--photo-mid) 50%,var(--photo-warm) 100%)}

  .reason{position:absolute;left:0;width:100%}
  .reason-num{position:absolute;width:25px;height:25px;border-radius:50%;background:var(--green);color:#fff;font-size:12px;display:flex;align-items:center;justify-content:center}
  .reason-icon{position:absolute;width:40px;height:40px}
  .reason-icon svg{width:100%;height:100%}
  .reason-title{position:absolute;font-size:11.8px;color:var(--green);font-weight:400;white-space:nowrap;-webkit-text-stroke:.2px var(--green)}
  .reason-text{position:absolute;font-size:9.6px;line-height:1.2;color:var(--text)}

  .sheet--front .reason-num{left:43px;top:7px}
  .sheet--front .reason-icon{left:74px;top:0}
  .sheet--front .reason-title{left:133px;top:0}
  .sheet--front .reason-text{left:133px;top:24px;width:312px}

  .sheet--back .reason-num{left:44px;top:7px}
  .sheet--back .reason-icon{left:83px;top:0;width:38px;height:38px}
  .sheet--back .reason-title{left:134px;top:0}
  .sheet--back .reason-text{left:134px;top:24px;width:312px}

  .footer{position:absolute;left:0;bottom:0;width:100%;height:41px;background:var(--charcoal);color:#fff;font-size:9.2px;display:flex;align-items:center;justify-content:center;gap:7px;white-space:nowrap}
  .footer-sep{color:#aaa}
</style>
</head>
<body>

<section class="sheet sheet--front" aria-label="Front">
  <h1 class="title">Top 10 Reasons</h1>
  <p class="subtitle">Why an FPP Serves Your Family Enterprise</p>
  <div class="brand"><span>QUORVANE</span><span class="brand-dot"></span></div>
  <div class="hero" role="img" aria-label="Photo of young green seedlings sprouting against a soft blurred background"></div>

  <article class="reason" style="top:289px">
    <span class="reason-num">1</span>
    <div class="reason-icon"><svg viewBox="0 0 40 40" fill="none" stroke="#3b3839" stroke-width="1.5"><rect x="5" y="5" width="22" height="30" rx="2"/><text x="8" y="17" font-size="8" fill="#83c242" stroke="none" font-family="sans-serif">TAX</text><path d="M9 22h12M9 26h12M9 30h8"/><path d="M34 14L22 30l-2 4 4-2 12-16z" stroke="#83c242"/></svg></div>
    <h2 class="reason-title">Create Significant Deductions</h2>
    <p class="reason-text">The FPP creates significant tax deductions, which can be used to keep the business under the small business rate or applied to the high rate, a bigger bang for the buck.</p>
  </article>

  <article class="reason" style="top:366px">
    <span class="reason-num">2</span>
    <div class="reason-icon"><svg viewBox="0 0 40 40" fill="none" stroke="#3b3839" stroke-width="1.5"><circle cx="15" cy="19" r="5"/><path d="M6 34c0-6 4-9 9-9s9 3 9 9z"/><path d="M24 8h6l-1 3c4 2 5 5 5 8h-14c0-3 1-6 5-8z" stroke="#83c242"/><rect x="26" y="24" width="9" height="3"/><rect x="26" y="28" width="9" height="3"/><rect x="26" y="32" width="9" height="3"/></svg></div>
    <h2 class="reason-title">Deliberate, Planned, Future Income</h2>
    <p class="reason-text">An income for beyond the last day at the office.</p>
  </article>

  <article class="reason" style="top:422px">
    <span class="reason-num">3</span>
    <div class="reason-icon"><svg viewBox="0 0 40 40" fill="none" stroke="#3b3839" stroke-width="1.5"><rect x="8" y="4" width="26" height="32" rx="2"/><path d="M12 10h14M12 14h10"/><path d="M14 30l6-6 4 3 7-8" stroke="#83c242"/><rect x="4" y="24" width="8" height="3"/><rect x="4" y="28" width="8" height="3"/><rect x="4" y="32" width="8" height="3"/></svg></div>
    <h2 class="reason-title">Past Buy Back</h2>
    <p class="reason-text">Most owners invest, first, in the business. The FPP offers the ability to go back and recover lost years when they did not buy RRSPs…and pass the tax savings onto their company.</p>
  </article>

  <article class="reason" style="top:501px">
    <span class="reason-num">4</span>
    <div class="reason-icon"><svg viewBox="0 0 40 40" fill="none" stroke="#3b3839" stroke-width="1.5"><circle cx="20" cy="12" r="7" stroke="#83c242"/><text x="17" y="15.5" font-size="9" fill="#83c242" stroke="none" font-family="sans-serif">$</text><path d="M4 16l3 12 8 8M36 16l-3 12-8 8"/><path d="M9 22l5 7M31 22l-5 7"/></svg></div>
    <h2 class="reason-title">Creditor Proof</h2>
    <p class="reason-text">All Assets held in an FPP are creditor proof, including RRSPs, and planned pension contributions receive “super-priority” status, which rank above the claims of secured creditors, like major commercial lenders and banks.</p>
  </article>

  <footer class="footer"><span>410 – 88 Harbour Lane, Brightwater, Saskatchewan, S4X 2B9</span><span class="footer-sep">|</span><span>1-800-555-0142 (Toll Free)</span><span class="footer-sep">|</span><span>quorvane.ca</span></footer>
</section>

<section class="sheet sheet--back" aria-label="Back">
  <h1 class="title">Top 10 Reasons</h1>
  <p class="subtitle">Why an FPP Serves Your Family Enterprise</p>
  <div class="brand"><span>QUORVANE</span><span class="brand-dot"></span></div>

  <article class="reason" style="top:89px">
    <span class="reason-num">5</span>
    <div class="reason-icon"><svg viewBox="0 0 40 40" fill="none" stroke="#3b3839" stroke-width="2"><path d="M20 36V6M15 11l5-5 5 5"/><path d="M20 24c-4-4-8-4-12-4M8 15v5h5"/><path d="M20 24c4-4 8-4 12-4M32 15v5h-5"/></svg></div>
    <h2 class="reason-title">Flexibility</h2>
    <p class="reason-text">Owners know that cash flows can swing wildly with the business cycle. An FPP offers the flexibility to flip between DB and DC accounts in order to conserve cash, smooth income during volatile years, and recover assets when things improve.</p>
  </article>

  <article class="reason" style="top:179px">
    <span class="reason-num">6</span>
    <div class="reason-icon"><svg viewBox="0 0 40 40" fill="none" stroke="#3b3839" stroke-width="1.5"><path d="M17 4h8l-2 4c5 2 7 6 7 10h-18c0-4 2-8 7-10z"/><text x="18" y="17" font-size="8" fill="#83c242" stroke="none" font-family="sans-serif">$</text><path d="M3 24h8l8 3h8c2 0 2 3 0 3h-9M3 34h8l10 2 14-8c1-2-1-3-3-2l-8 4"/></svg></div>
    <h2 class="reason-title">Preserve the Lifetime Capital Gains Exemption</h2>
    <p class="reason-text">Create $1.6 Million++ of Tax Free Capital Gains. The significant deductions created in an FPP can be used to purify a corporation with passive assets, which can help preserve the shareholders’ lifetime capital gains exemption.</p>
  </article>

  <article class="reason" style="top:269px">
    <span class="reason-num">7</span>
    <div class="reason-icon"><svg viewBox="0 0 40 40" fill="none" stroke-width="1.8"><rect x="5" y="13" width="30" height="14" rx="1" stroke="#3b3839" stroke-width="2.2"/><text x="17" y="24" font-size="10" fill="#3b3839" font-family="sans-serif">$</text><path d="M12 8c5-4 11-4 16 0M28 8l-3-2M12 32c5 4 11 4 16 0M12 32l3 2" stroke="#83c242"/></svg></div>
    <h2 class="reason-title">Intergenerational Wealth Transfer</h2>
    <p class="reason-text">Unlike RRSPs that eventually trigger a taxable disposition upon death, an FPP has the ability to pass, tax deferred, to the next generation of family business owners.</p>
  </article>

  <article class="reason" style="top:346px">
    <span class="reason-num">8</span>
    <div class="reason-icon"><svg viewBox="0 0 40 40" fill="none"><path d="M34 20A14 14 0 1 1 26 7" stroke="#83c242" stroke-width="2.2"/><path d="M24 4l4 3-3 4" stroke="#83c242" stroke-width="2"/><text x="10" y="23" font-size="8" fill="#3b3839" font-family="sans-serif" font-weight="bold">AGE</text></svg></div>
    <h2 class="reason-title">All Ages</h2>
    <p class="reason-text">An FPP can benefit all entrepreneurs between ages 18-71.</p>
  </article>

  <article class="reason" style="top:405px">
    <span class="reason-num">9</span>
    <div class="reason-icon"><svg viewBox="0 0 40 40" fill="none" stroke="#3b3839" stroke-width="1.5"><path d="M5 18a15 12 0 0 1 30 0z"/><path d="M20 6v22c0 3-4 3-4 0M13 18l2-10M27 18l-2-10"/><circle cx="11" cy="28" r="3.5" stroke="#83c242"/><circle cx="29" cy="28" r="3.5" stroke="#83c242"/></svg></div>
    <h2 class="reason-title">Conserve the Small Business Deduction</h2>
    <p class="reason-text">Investment income inside an FPP grows tax exempt and does not create passive income as outlined under the 2018 “Passive Income Measures”. Therefore, business owners that redirect corporate resources to fund their pension assets will not jeopardize their low corporate tax rate on profits and in associated companies.</p>
  </article>

  <article class="reason" style="top:505px">
    <span class="reason-num">10</span>
    <div class="reason-icon"><svg viewBox="0 0 40 40" fill="none" stroke="#3b3839" stroke-width="1.6"><rect x="5" y="5" width="8" height="8"/><rect x="16" y="5" width="8" height="8"/><rect x="27" y="5" width="8" height="8" fill="#83c242" stroke="#83c242"/><rect x="5" y="16" width="8" height="8"/><rect x="16" y="16" width="8" height="8"/><rect x="27" y="16" width="8" height="8"/><rect x="5" y="27" width="8" height="8"/><rect x="16" y="27" width="8" height="8"/><rect x="27" y="27" width="8" height="8"/></svg></div>
    <h2 class="reason-title">Broader Investment Options</h2>
    <p class="reason-text">An FPP allows entrepreneurs to invest in what they like: real estate, other businesses and/or franchises, private equity, public equity, exempt markets, etc. The possibilities are up to the imagination of the entrepreneur and their advisors.</p>
  </article>

  <footer class="footer"><span>410 – 88 Harbour Lane, Brightwater, Saskatchewan, S4X 2B9</span><span class="footer-sep">|</span><span>1-800-555-0142 (Toll Free)</span><span class="footer-sep">|</span><span>quorvane.ca</span></footer>
</section>

</body>
</html>
```